energy rating company

Web Design graphics and layout only

To create two pages for the website. First the home page and the second is the design for the job board for our clients use after login. I have attached files that explain in detail what the pages should have and the purpose/desires of each object. Please read these thoroughly.

The webpages need to be clean, professional, easy on the eye, obvious in all its buttons and functions with a strong call to action on the home page and branding and clean, great and obvious looking buttons and very simple but dynamic as well. We wish to be seen as contemporary.

Business Concept

Our business concept is simple, to build a website whereby our clients will be able to upload jobs for energy raters to quote on and subsequent complete the work if their quote is selected. To link energy ratings that are required with energy raters via our website. Similarly to the varn website, jobs will be “advertised” on the job board and raters will select which jobs they wish to quote for.

I have attached a Word document explaining all the parts of the website and another word document showing what we are sort of after and a excel spreadsheet as well. Please read these in conjunction with this brief!
Updates

Dear All

I have submitted with my brief a word doc and excel spreadsheet of the two pages I want created.  However this is not the layout or design I want, I only put it together so that you will need to know what is required on each page.  Feel free to change and redesign it all.

Also the second page does not require the "process" logo or any other menu items except the first five being Home, How it works, About Us, testimonials and Contact us as per the home page.

We also are looking for something very professional and very clean.  It should be very easy to see exactly what you are looking for.

I will also extend the deadline for new designers!!  I am excited to see your talents!!

Thanks

I have increase budget and posted a note saying feel free to change all the details layout etc on my brief just include everything!!! 

Wanting a professional corporate look...

Want a professional corporate look

We have changed our minds and you we no longer require the process to be on the home page.

Thanks

Target Market(s)

Target Market

Home Inspection Companies
Pest Inspection Companies
Residential home buyers/sellers
Real Estate companies

Industry/Entity Type

It Company

Number of Pages Required

1 page

Requirements
Must have
• Colours and Styles

• The website should be mainly white as I believe it is seen as clean and simple with colour from the logos, but can be swayed if it projects the image we are after.

• It should be obvious and process orientated and I do believe symbols, pictures, etc should replace words where possible.

```html
<!DOCTYPE html>
<html lang="en">
<head>
<meta charset="utf-8">
<title>Solvra – My Account</title>
<link rel="stylesheet" href="https://fonts.googleapis.com/css2?family=Source+Sans+3:ital,wght@0,400;0,600;0,700;1,400&display=swap">
<style>
  :root{
    --orange:#c05a12;
    --green-text:#2f8d1f;
    --green-top:#4ea41d;
    --green-bottom:#a6ca18;
    --grey-panel:#eeeeee;
    --text:#555;
    --page:#ffffff;
    --backdrop:#e9e9e9;
  }
  *{box-sizing:border-box;margin:0;padding:0}
  html,body{width:1010px;height:1200px;overflow:hidden}
  body{background:var(--backdrop);font-family:"Source Sans 3",sans-serif;color:var(--text)}
  .page{position:relative;width:1010px;height:1200px;background:linear-gradient(#fff 0,#fff 85%,#f1f1f1 100%)}
  .abs{position:absolute}

  .brand{left:96px;top:44px;display:flex;align-items:center;gap:12px}
  .brand-dot{width:54px;height:54px;border-radius:50%;background:var(--green-bottom)}
  .brand-name{font-size:46px;font-weight:700;color:var(--orange);letter-spacing:-0.5px;line-height:1}

  .user-links{right:99px;top:76px;font-size:11px}
  .user-links a{text-decoration:none;color:var(--orange)}
  .user-links .who{color:var(--green-text)}
  .user-links .sep{color:var(--orange);margin:0 3px}

  .card{left:29px;top:136px;width:950px;height:965px;background:#fff;border-radius:10px;box-shadow:0 0 6px rgba(0,0,0,.25);overflow:hidden}
  .nav{display:flex;font-size:14px;color:#555}
  .nav span{margin-right:14px}
  .card .nav{position:absolute;left:67px;top:24px}
  .search{position:absolute;right:72px;top:18px;width:158px;height:26px;border-radius:13px;background:#fff;box-shadow:inset 0 1px 3px rgba(0,0,0,.3),0 1px 2px rgba(0,0,0,.15)}
  .search svg{position:absolute;left:9px;top:5px}

  .account-panel{position:absolute;left:0;top:68px;width:950px;height:445px;background:var(--grey-panel)}

  .section-bar{position:absolute;left:55px;width:840px;height:52px;border-radius:8px;background:linear-gradient(var(--green-top),var(--green-bottom));display:flex;align-items:center;padding-left:28px;gap:12px;color:#fff;font-size:29px}
  .bar-dot{width:30px;height:30px;border-radius:50%;border:2px solid rgba(255,255,255,.8)}

  .details{position:absolute;left:64px;top:176px;font-size:14px}
  .details h2{font-size:16px;font-weight:400;color:var(--orange);margin-bottom:17px}
  .row{display:flex;min-height:35px}
  .row dt{width:135px;font-style:italic;color:var(--green-text)}
  .row dd{color:var(--text);line-height:18px}

  .tabs{position:absolute;left:55px;top:617px;display:flex;gap:16px}
  .tab{width:187px;height:57px;border-radius:12px;background:linear-gradient(var(--green-top),var(--green-bottom));color:#fff;font-size:15px;display:flex;align-items:center;justify-content:center;box-shadow:0 1px 2px rgba(0,0,0,.2)}

  .jobs-table{left:0;top:845px;width:1010px}
  .tr{display:grid;grid-template-columns:194px 68px 62px 66px 90px 73px 100px 37px 99px 19px 99px;align-items:center}
  .th{color:var(--orange);font-size:13px;line-height:16px;text-align:right;margin-bottom:16px}
  .th > span{display:block}
  .td{font-size:10px;height:19.5px;text-align:right;color:var(--text)}
  .td > span{display:block}
  .td .job{color:var(--green-text)}
  .btn{height:12px;border-radius:6px;background:linear-gradient(var(--green-top),var(--green-bottom));color:#fff;font-size:9.5px;line-height:12px;text-align:center}
  .group{margin-bottom:19px}

  .footer .nav{position:absolute;left:96px;top:1128px}
  .copyright{position:absolute;right:93px;top:1131px;font-size:11px;font-style:italic;color:#555}
</style>
</head>
<body>
<div class="page">
  <div class="brand abs">
    <div class="brand-dot"></div>
    <div class="brand-name">solvra</div>
  </div>

  <div class="user-links abs"><span class="who">Logged in as Sam Tran</span><span class="sep">|</span><a href="#">My Account</a><span class="sep">|</span><a href="#">Log out</a></div>

  <div class="card abs">
    <nav class="nav"><span>Home</span><span>How it works?</span><span>About Us</span><span>Testimonials</span><span>Contact Us</span><span>Help</span></nav>
    <div class="search"><svg width="16" height="16" viewBox="0 0 16 16"><circle cx="6.5" cy="6.5" r="4.5" fill="none" stroke="#bbb" stroke-width="1.6"/><line x1="10" y1="10" x2="14" y2="14" stroke="#bbb" stroke-width="2"/></svg></div>

    <div class="account-panel">
      <div class="section-bar" style="top:22px"><span class="bar-dot"></span>My Account</div>
      <div class="details" style="top:106px">
        <h2>Personal Details</h2>
        <dl>
          <div class="row"><dt>Company Details</dt><dd></dd></div>
          <div class="row"><dt>Contact Person</dt><dd>Sam Tran</dd></div>
          <div class="row"><dt>Email Address</dt><dd></dd></div>
          <div class="row" style="min-height:54px"><dt>Street Address</dt><dd>Level 1<br>82 Harlow Street</dd></div>
          <div class="row"><dt>Suburb</dt><dd>Elmvale</dd></div>
          <div class="row"><dt>State</dt><dd>VIC</dd></div>
          <div class="row"><dt>Postcode</dt><dd>3999</dd></div>
        </dl>
      </div>
    </div>

    <div class="section-bar" style="top:539px"><span class="bar-dot"></span>Jobs</div>
    <div class="tabs"><div class="tab">Jobs for quoting</div><div class="tab">Active Jobs</div><div class="tab">Completed Jobs</div></div>
  </div>

  <div class="jobs-table abs">
    <div class="tr th"><span>Job</span><span>Quote<br>Number</span><span>Price</span><span>Total<br>Price</span><span>Turnaround<br>Time</span><span>Rework<br>price</span><span>Energy Raters<br>Accreditation</span></div>

    <div class="group">
      <div class="tr td"><span class="job">Mira Court</span><span>111111</span><span>$155,00</span><span>$180,65</span><span>1-5 days</span><span>$120,00</span><span>VIC</span><span></span><span class="btn">Accept /Decline</span><span></span><span class="btn">Email Energy Rater</span></div>
      <div class="tr td"><span></span><span>111156</span><span>$250,00</span><span>$265,00</span><span>5-10 days</span><span>$150,00</span><span>QLD</span><span></span><span class="btn">Accept /Decline</span><span></span><span class="btn">Email Energy Rater</span></div>
      <div class="tr td"><span></span><span>111186</span><span>$125,00</span><span>$129,65</span><span>2 weeks</span><span>$100,00</span><span>SA</span><span></span><span class="btn">Accept /Decline</span><span></span><span class="btn">Email Energy Rater</span></div>
    </div>

    <div class="group">
      <div class="tr td"><span class="job">Mira Court</span><span>111111</span><span>$155,00</span><span>$180,65</span><span>1-5 days</span><span>$120,00</span><span>VIC</span><span></span><span class="btn">Accept /Decline</span><span></span><span class="btn">Email Energy Rater</span></div>
      <div class="tr td"><span></span><span>111156</span><span>$250,00</span><span>$265,00</span><span>5-10 days</span><span>$150,00</span><span>QLD</span><span></span><span class="btn">Accept /Decline</span><span></span><span class="btn">Email Energy Rater</span></div>
      <div class="tr td"><span></span><span>111186</span><span>$125,00</span><span>$129,65</span><span>2 weeks</span><span>$100,00</span><span>SA</span><span></span><span class="btn">Accept /Decline</span><span></span><span class="btn">Email Energy Rater</span></div>
      <div class="tr td"><span></span><span>111313</span><span>$350,00</span><span>$354,65</span><span>Aluminum</span><span>Doors</span><span>Standard</span><span></span><span class="btn">Accept /Decline</span><span></span><span class="btn">Email Energy Rater</span></div>
    </div>
  </div>

  <footer class="footer">
    <nav class="nav"><span>Home</span><span>How it works?</span><span>About Us</span><span>Testimonials</span><span>Contact Us</span><span>Help</span></nav>
    <div class="copyright">Copyright © 2010 solvra. All rights reserved.</div>
  </footer>
</div>
</body>
</html>
```